New London based construction company website

We need a website designing for our new London based construction company which aims to provide total & brackley yard services.

The website is to have two sides to it one for "fernway yard services" and one for "brackley yard services" with an opening page with both logo's to choose from.

Would like the website to be modern, professional and inspire confidence.

Target Market(s)

Those specifically visiting the site to check that the company is professional

Industry/Entity Type

Construction

Contact Information for Business Card

One side for Brackley Yard Services the other Fernway Yard Services

Number of Pages Required

5+ page

Font styles to use
Sans Serif

Requirements
Must have
• The website is to have two sides to it one for "fernway yard services" and one for "brackley yard services" with an opening page with both logo's to choose from.

```html
<!DOCTYPE html>
<html lang="en">
<head>
<meta charset="utf-8">
<title>Fernway &amp; Brackley Yard Services</title>
<link rel="stylesheet" href="https://fonts.googleapis.com/css2?family=Roboto:wght@300;400;500&display=swap">
<style>
  :root {
    --bg-top: #2152ad;
    --bg-mid: #2458b8;
    --bg-bottom: #1d4797;
    --grid-line: rgba(255, 255, 255, 0.16);
    --tick: #ffffff;
    --card: #ffffff;
    --brand-blue: #1a5c9a;
    --ink: #1e1e1e;
    --photo-light: #5b95d6;
    --photo-dark: #1b3f8f;
  }
  * { margin: 0; padding: 0; box-sizing: border-box; }
  html, body { width: 1200px; height: 781px; overflow: hidden; }
  body {
    position: relative;
    font-family: "Roboto", sans-serif;
    background: linear-gradient(180deg, var(--bg-top) 0%, var(--bg-mid) 35%, var(--bg-bottom) 100%);
  }
  .grid-line {
    position: absolute; top: 0; bottom: 0; width: 1px;
    background: var(--grid-line);
  }
  .ruler {
    position: absolute; top: 0; left: 0; width: 499px; height: 19px;
  }
  .ruler-minor {
    position: absolute; top: 0; left: 0; right: 0; height: 6px;
    background: repeating-linear-gradient(90deg, var(--tick) 0 1.5px, transparent 1.5px 17.44px);
    background-position: 7.8px 0;
  }
  .ruler-major {
    position: absolute; top: 0; left: 0; right: 0; height: 10px;
    background: repeating-linear-gradient(90deg, var(--tick) 0 1.5px, transparent 1.5px 87.2px);
    background-position: 60px 0;
  }
  .ruler-end {
    position: absolute; top: 0; left: 497px; width: 1.5px; height: 19px; background: var(--tick);
  }
  .site-photo {
    position: absolute; left: 960px; top: 150px; width: 240px; height: 631px;
    background: radial-gradient(ellipse 90% 60% at 85% 45%, var(--photo-light) 0%, rgba(60,120,200,0.6) 45%, rgba(30,70,150,0) 80%),
                linear-gradient(180deg, rgba(27,63,143,0) 40%, var(--photo-dark) 100%);
  }
  .choice-card {
    position: absolute;
    background: var(--card);
  }
  .card-fernway { left: 322px; top: 96px; width: 396px; height: 270px; }
  .card-brackley { left: 498px; top: 406px; width: 422px; height: 253px; }
  .brand-name {
    display: flex; align-items: center; gap: 14px;
    position: absolute;
    font-weight: 400; font-size: 25px; letter-spacing: 0.5px;
    color: var(--brand-blue);
    white-space: nowrap;
  }
  .brand-mark { width: 44px; height: 44px; background: var(--brand-blue); flex: none; }
  .card-fernway .brand-name { left: 20px; top: 26px; }
  .card-brackley .brand-name { left: 34px; top: 26px; }
  .card-text {
    position: absolute;
    font-weight: 300; font-size: 15.7px; line-height: 20px; color: var(--ink);
  }
  .card-fernway .card-text { left: 27px; top: 122px; }
  .card-brackley .card-text { left: 31px; top: 122px; }
  .visit-button {
    position: absolute;
    width: 124px; height: 39px;
    border: 2px solid var(--brand-blue);
    color: var(--brand-blue);
    font-size: 15.5px; font-weight: 400;
    display: flex; align-items: center; justify-content: center;
    text-decoration: none;
  }
  .card-fernway .visit-button { left: 26px; top: 177px; }
  .card-brackley .visit-button { left: 31px; top: 178px; }
</style>
</head>
<body>
  <div class="grid-line" style="left:322px"></div>
  <div class="grid-line" style="left:498px"></div>
  <div class="grid-line" style="left:673px"></div>
  <div class="grid-line" style="left:848px"></div>
  <div class="grid-line" style="left:1022px"></div>

  <div class="ruler">
    <div class="ruler-minor"></div>
    <div class="ruler-major"></div>
    <div class="ruler-end"></div>
  </div>

  <div class="site-photo" role="img" aria-label="Tower crane above a building under construction, tinted blue"></div>

  <section class="choice-card card-fernway">
    <div class="brand-name"><span class="brand-mark"></span>Fernway Yard Services</div>
    <p class="card-text">Lorem ipsum dolor sit amet, consectetur<br>adipiscing elit, sed do eiusmod.</p>
    <a class="visit-button" href="#">VISIT SITE</a>
  </section>

  <section class="choice-card card-brackley">
    <div class="brand-name"><span class="brand-mark"></span>Brackley Yard Services</div>
    <p class="card-text">Lorem ipsum dolor sit amet, consectetur<br>adipiscing elit, sed do eiusmod.</p>
    <a class="visit-button" href="#">VISIT SITE</a>
  </section>
</body>
</html>
```